" A empresa é de pequeno porte, atende projetos únicos de móveis planejados com fino acabamento e design moderno de acordo com a demanda dos arquitetos. "

```html
<!DOCTYPE html>
<html lang="pt-BR">
<head>
<meta charset="UTF-8">
<title>Lirenza – Adesivo</title>
<link rel="stylesheet" href="https://fonts.googleapis.com/css2?family=Montserrat:wght@400;500&display=swap">
<style>
  :root {
    --page-bg: #e4e4e4;
    --sticker-bg: #ffffff;
    --sticker-border: #1c1c1c;
    --brand-dark: #2b201d;
    --brand-gold: #b8894f;
    --contact-text: #3a3a3a;
  }
  * { margin: 0; padding: 0; box-sizing: border-box; }
  html, body {
    width: 1200px;
    height: 1200px;
    overflow: hidden;
    background: var(--page-bg);
    font-family: "Montserrat", sans-serif;
  }
  .sticker {
    position: absolute;
    left: 180px;
    top: 449px;
    width: 840px;
    height: 336px;
    background: var(--sticker-bg);
    border: 8px solid var(--sticker-border);
    border-radius: 34px;
  }
  .brand {
    position: absolute;
    left: 95px;
    top: 95px;
    display: flex;
    align-items: center;
    gap: 26px;
  }
  .brand-square {
    width: 96px;
    height: 96px;
    background: var(--brand-gold);
  }
  .brand-name {
    font-weight: 500;
    font-size: 68px;
    letter-spacing: 14px;
    color: var(--brand-dark);
    line-height: 1;
  }
  .contacts {
    position: absolute;
    left: 95px;
    right: 95px;
    top: 240px;
    display: flex;
    justify-content: space-between;
    align-items: center;
    list-style: none;
  }
  .contact {
    display: flex;
    align-items: center;
    gap: 8px;
    font-size: 12px;
    color: var(--contact-text);
  }
  .contact-icon {
    width: 14px;
    height: 14px;
    flex: none;
  }
</style>
</head>
<body>
  <div class="sticker">
    <div class="brand">
      <span class="brand-square"></span>
      <span class="brand-name">LIRENZA</span>
    </div>
    <ul class="contacts">
      <li class="contact">
        <svg class="contact-icon" viewBox="0 0 14 14"><path d="M3 1h2l1 3-1.5 1a7 7 0 0 0 4.5 4.5L10 8l3 1v2a2 2 0 0 1-2 2A10 10 0 0 1 1 3a2 2 0 0 1 2-2z" fill="#2b201d"/></svg>
        (00) 00000-0000
      </li>
      <li class="contact">
        <svg class="contact-icon" viewBox="0 0 14 14"><rect x="1" y="1" width="12" height="12" rx="2" fill="#2b201d"/></svg>
        @instagram
      </li>
      <li class="contact">
        <svg class="contact-icon" viewBox="0 0 14 14"><rect x="1" y="1" width="12" height="12" rx="2" fill="#2b201d"/></svg>
        /facebook
      </li>
      <li class="contact">
        <svg class="contact-icon" viewBox="0 0 14 14"><rect x="1" y="3" width="12" height="8" rx="1" fill="none" stroke="#2b201d" stroke-width="1.5"/><path d="M1.5 3.5 7 8l5.5-4.5" fill="none" stroke="#2b201d" stroke-width="1.5"/></svg>
        email@email.com.br
      </li>
      <li class="contact">
        <svg class="contact-icon" viewBox="0 0 14 14"><circle cx="7" cy="7" r="5.5" fill="none" stroke="#2b201d" stroke-width="1.5"/><path d="M1.5 7h11M7 1.5c-2.5 3-2.5 8 0 11M7 1.5c2.5 3 2.5 8 0 11" fill="none" stroke="#2b201d" stroke-width="1.2"/></svg>
        www.site.com.br
      </li>
    </ul>
  </div>
</body>
</html>
```